Facebook - Cover and profile picture

Hey, we need a cover pic and a picure for our sportsmanagement agency. I have uploaded a couple of files: Our Logo, our main Color, our old Picture Picture, which should be integrated into the cover Picture. We look forward to seeing your creative designs. If you have any questions, just ask.

```html
<!DOCTYPE html>
<html lang="de">
<head>
<meta charset="utf-8">
<title>NORVA – Facebook Titelbild und Profilbild</title>
<link rel="stylesheet" href="https://fonts.googleapis.com/css2?family=Bebas+Neue&family=Montserrat:wght@600&display=swap">
<style>
  :root {
    --page-bg: #e9ebef;
    --brand-blue: #03a3d8;
    --navy: #1b1d55;
    --navy-deep: #15174a;
    --white: #ffffff;
    --ink: #15151a;
    --frame-line: #d6d9e0;
  }
  * { margin: 0; padding: 0; box-sizing: border-box; }
  html, body {
    width: 800px;
    height: 1200px;
    overflow: hidden;
    background: var(--page-bg);
  }
  .canvas {
    position: relative;
    width: 800px;
    height: 1200px;
  }

  /* Profile picture */
  .profile {
    position: absolute;
    left: 300px;
    top: 330px;
    width: 200px;
    height: 200px;
    background: var(--white);
    border: 1px solid var(--frame-line);
    box-shadow: 0 10px 30px rgba(20, 25, 60, 0.14);
    display: flex;
    align-items: center;
    justify-content: center;
  }
  .profile-brand {
    font-family: "Montserrat", sans-serif;
    font-weight: 600;
    font-size: 32px;
    letter-spacing: 1px;
    color: var(--ink);
  }

  /* Cover */
  .cover {
    position: absolute;
    left: 83px;
    top: 717px;
    width: 635px;
    height: 241px;
    overflow: hidden;
  }
  .cover-backdrop {
    position: absolute;
    inset: 0;
    width: 100%;
    height: 100%;
  }
  .cover-watermark {
    position: absolute;
    left: 0;
    top: 156px;
    font-family: "Montserrat", sans-serif;
    font-weight: 600;
    font-size: 46px;
    line-height: 1;
    color: rgba(255, 255, 255, 0.16);
  }
  .cover-team-photo {
    position: absolute;
    left: 157px;
    top: 33px;
    width: 257px;
    height: 190px;
    border-radius: 14px 14px 4px 4px;
    background: linear-gradient(180deg,
      rgba(236, 236, 240, 0.88) 0%,
      rgba(222, 222, 228, 0.85) 40%,
      rgba(40, 40, 48, 0.88) 55%,
      rgba(22, 22, 28, 0.92) 100%);
  }
  .cover-headline {
    position: absolute;
    left: 421px;
    top: 17px;
    width: 200px;
    text-align: center;
    font-family: "Bebas Neue", sans-serif;
    font-weight: 400;
    font-size: 22px;
    line-height: 28px;
    color: var(--white);
  }
  .cover-brand {
    position: absolute;
    left: 421px;
    top: 155px;
    width: 200px;
    text-align: center;
    font-family: "Montserrat", sans-serif;
    font-weight: 600;
    font-size: 26px;
    line-height: 1;
    letter-spacing: 1px;
    color: var(--white);
  }
</style>
</head>
<body>
<main class="canvas">

  <section class="profile" aria-label="Facebook-Profilbild">
    <p class="profile-brand">NORVA</p>
  </section>

  <section class="cover" aria-label="Facebook-Titelbild">
    <svg class="cover-backdrop" viewBox="0 0 1244 473" preserveAspectRatio="none" role="img" aria-label="Stadion bei Flutlicht mit Rasen, übergehend in Markenblau und Dunkelblau">
      <defs>
        <linearGradient id="stadium-sky" x1="0" y1="0" x2="0" y2="1">
          <stop offset="0" stop-color="#5b3f52"/>
          <stop offset="0.5" stop-color="#3a2d4a"/>
          <stop offset="1" stop-color="#2b3a3e"/>
        </linearGradient>
        <radialGradient id="flood-left" cx="0.18" cy="0.05" r="0.35">
          <stop offset="0" stop-color="#f0a070" stop-opacity="0.85"/>
          <stop offset="1" stop-color="#d9855a" stop-opacity="0"/>
        </radialGradient>
        <radialGradient id="flood-center" cx="0.5" cy="0.12" r="0.3">
          <stop offset="0" stop-color="#f4e3c4" stop-opacity="0.85"/>
          <stop offset="1" stop-color="#f4e3c4" stop-opacity="0"/>
        </radialGradient>
        <linearGradient id="navy-panel" x1="0" y1="0" x2="1" y2="0">
          <stop offset="0" stop-color="#1b1d55" stop-opacity="0"/>
          <stop offset="0.25" stop-color="#1b1d55" stop-opacity="0.92"/>
          <stop offset="1" stop-color="#15174a"/>
        </linearGradient>
        <linearGradient id="pitch" x1="0" y1="0" x2="0" y2="1">
          <stop offset="0" stop-color="#6f8a4e"/>
          <stop offset="1" stop-color="#2f5a3c"/>
        </linearGradient>
      </defs>
      <rect width="1244" height="473" fill="url(#stadium-sky)"/>
      <rect x="300" y="220" width="700" height="253" fill="url(#pitch)"/>
      <rect width="1244" height="473" fill="url(#flood-left)"/>
      <rect width="1244" height="473" fill="url(#flood-center)"/>
      <rect x="780" y="0" width="464" height="473" fill="url(#navy-panel)"/>
      <path fill="#2d4a44" d="M800 300 L850 270 L900 290 L960 260 L1010 300 L1040 360 L1060 420 L1100 473 L800 473 Z"/>
      <path fill="#03a3d8" d="M0 105 L30 98 L55 110 L90 95 L120 112 L160 100 L200 118 L240 150 L270 170 L300 200 L320 240 L340 300 L380 330 L460 350 L560 360 L640 350 L720 340 L780 330 L800 350 L820 390 L850 400 L880 410 L930 425 L1000 440 L1060 445 L1110 460 L1140 473 L0 473 Z"/>
    </svg>

    <div class="cover-watermark" aria-hidden="true">NORVA</div>
    <div class="cover-team-photo" role="img" aria-label="Gruppenfoto des fünfköpfigen Agenturteams in weißen Hemden, einer hält einen Fußball"></div>

    <h1 class="cover-headline">Sportberatung und<br>Spielervermittlung</h1>
    <p class="cover-brand">NORVA</p>
  </section>

</main>
</body>
</html>
```